Slider created for Warm Kettle Kitchen

We need a new slider created for our Warm Kettle Kitchen website (www.warmkettlekitchen.com.au). Warm Kettle Kitchen is a central place where people who love food, cooking for their family and sharing recipes can hang out. We'd like the sliders to look more 'earthy' than the ones currently used - and more like our Facebook style https://www.facebook.com/WarmKettleKitchen .
The first slider we'd like to create will point to the blog on the website with the following:
Text: In Season Now - Ruby Red Grapefruit
Image: Ruby Red Grapefruit
The slider is 990 X 225 pixels.

```html
<!DOCTYPE html>
<html lang="en">
<head>
<meta charset="utf-8">
<title>Warm Kettle Kitchen – In Season Now: Ruby Red Grapefruit</title>
<link rel="stylesheet" href="https://fonts.googleapis.com/css2?family=Lobster+Two:ital,wght@1,700&family=Signika:wght@300;600&display=swap">
<style>
  :root {
    --page-bg: #d9d9d9;
    --band-yellow: #f5b400;
    --band-orange: #ec9418;
    --band-deep: #e47f1f;
    --photo-coral: #ee6f5a;
    --photo-rind: #f3a34e;
    --text-light: #ffffff;
    --button-cream: #fdf1dc;
    --button-edge: #5a2e17;
    --button-text: #d42a1c;
  }
  * { box-sizing: border-box; margin: 0; padding: 0; }
  html, body {
    width: 1200px;
    height: 404px;
    overflow: hidden;
    background: var(--page-bg);
  }
  .canvas {
    position: relative;
    width: 1200px;
    height: 404px;
  }
  .slider {
    position: absolute;
    left: 114px;
    top: 74px;
    width: 970px;
    height: 220px;
    overflow: hidden;
    background: linear-gradient(90deg, var(--band-yellow) 0%, var(--band-yellow) 58%, var(--band-orange) 80%, var(--band-deep) 100%);
  }
  .slider__photo {
    position: absolute;
    left: 0;
    top: 0;
    width: 580px;
    height: 220px;
    background: linear-gradient(90deg, var(--photo-coral) 0%, var(--photo-rind) 55%, var(--photo-coral) 85%, rgba(238, 111, 90, 0) 100%);
  }
  .slider__copy {
    position: absolute;
    left: 594px;
    top: 0;
    width: 300px;
    height: 220px;
    text-align: center;
    color: var(--text-light);
  }
  .slider__kicker {
    position: absolute;
    left: 0;
    right: 0;
    top: 38px;
    font-family: "Lobster Two", cursive;
    font-style: italic;
    font-weight: 700;
    font-size: 30px;
    line-height: 40px;
  }
  .slider__title {
    position: absolute;
    left: 0;
    right: 0;
    top: 88px;
    font-family: "Signika", sans-serif;
    font-weight: 300;
    font-size: 31px;
    line-height: 40px;
  }
  .slider__button {
    position: absolute;
    left: 71px;
    top: 147px;
    width: 158px;
    height: 36px;
    border: 4px solid var(--button-edge);
    border-radius: 18px;
    background: linear-gradient(180deg, #ffffff 0%, var(--button-cream) 55%, #efcfa3 100%);
    font-family: "Signika", sans-serif;
    font-weight: 600;
    font-size: 17px;
    line-height: 28px;
    color: var(--button-text);
    text-decoration: none;
    display: block;
  }
</style>
</head>
<body>
  <div class="canvas">
    <section class="slider">
      <div class="slider__photo" role="img" aria-label="Photo of halved and wedged ruby red grapefruit"></div>
      <div class="slider__copy">
        <p class="slider__kicker">In Season Now</p>
        <h1 class="slider__title">Ruby Red Grapefruit</h1>
        <a class="slider__button" href="#">Read More</a>
      </div>
    </section>
  </div>
</body>
</html>
```